New young doctors office business card

Doctor's office
Hello:
My name is Dr. Eduardo Maximino Ortega Benavides. I need a business card for my new office located within a hospital. The name of the hospital is "Hospital Almendral". Although the hospital logo and name must be included in the business card, please make me a personal logo for myself. The logo might be maybe my name in a stylish font, or my initials (EMOB) or something like that. Im more inclined to a font logo, rather than a image logo, but a good one might change my mind. The info on my business card is going to be in spanish. The following info must be included please (the info within parenthesis is not to be included, it is provided for you to understand it since it's in spanish, so you can properly place it on the card):
-Dr. Eduardo Maximino Ortega Benavides (my name)
-Medicina general (My specialty)
-Hospital Almendral (The name of the hospital where my office is)
-Calle Tomás Ocampo #247 Col. Almendral (address)
-Tel 471-5836 (Office phone)
-Sábado y domingo 10:00 am a 10:00pm (Office hours)
-Emergencias: 555-917-4402 (Emergency phone)
-maximinoob@correoficticio.mx (email)
-English Spoken
So, that's all the info i need to be on the business card. Although it's a business card for a doctor's office, i dont want it to be a boring, plain business card. Make it eye-catchy and stylish please. As i said, the hospital logo must be included. You'll find it on the heading of the PDF file i attached, but dont make it the center of attention.
Physician
Hello:My name is Dr. Eduardo Maximino Ortega Benavides. I need a business card for my new office located within a hospital. The name of the hospital is "Hospital Almendral". Although the hospital logo and name must be included in the business card, please make me a personal logo for myself. The logo might be maybe my name in a stylish font, or my initials (EMOB) or something like that. Im more inclined to a font logo, rather than a image logo, but a good one might change my mind. The info on my business card is going to be in spanish. The following info must be included please (the info within parenthesis is not to be included, it is provided for you to understand it since it's in spanish, so you can properly place it on the card):-Dr. Eduardo Maximino Ortega Benavides (my name)-Medicina general (My specialty)-Hospital Almendral (The name of the hospital where my office is)-Calle Tomás Ocampo #247 Col. Almendral (address)-Tel 471-5836 (Office phone)-Sábado y domingo 10:00 am a 10:00pm (Office hours)-Emergencias: 555-917-4402 (Emergency phone)-maximinoob@correoficticio.mx (email)-English Spoken So, that's all the info i need to be on the business card. Although it's a business card for a doctor's office, i dont want it to be a boring, plain business card. Make it eye-catchy and stylish please. As i said, the hospital logo must be included. You'll find it on the heading of the PDF file i attached, but dont make it the center of attention.

```html
<!DOCTYPE html>
<html lang="es">
<head>
<meta charset="utf-8">
<title>Dr. Eduardo Maximino Ortega Benavides — Tarjeta</title>
<link rel="stylesheet" href="https://fonts.googleapis.com/css2?family=Bitter:wght@800&family=Arimo:wght@400&family=Roboto+Condensed:wght@400;700&display=swap">
<style>
  :root {
    --card-blue: #253a78;
    --ink-white: #ffffff;
    --accent-yellow: #f4e21c;
    --edge-grey: #8a8fa3;
  }
  html, body {
    margin: 0;
    padding: 0;
    width: 721px;
    height: 1200px;
    overflow: hidden;
    background: var(--card-blue);
  }
  .card {
    position: relative;
    width: 721px;
    height: 1200px;
    box-sizing: border-box;
    background: var(--card-blue);
    border: 1px solid var(--edge-grey);
    color: var(--ink-white);
    font-family: "Arimo", Arial, sans-serif;
  }
  .card > * { position: absolute; margin: 0; line-height: 1; white-space: nowrap; }

  .doctor-name {
    left: 85px;
    top: 72px;
    font-family: "Bitter", Georgia, serif;
    font-weight: 800;
    font-size: 64px;
    line-height: 85px;
    letter-spacing: 0.5px;
  }
  .doctor-name span { display: block; }

  .specialty {
    left: 85px;
    top: 410px;
    font-size: 30px;
    line-height: 38px;
    color: var(--accent-yellow);
  }
  .specialty span { display: block; }

  .hours {
    left: 79px;
    top: 508px;
    font-family: "Roboto Condensed", "Arial Narrow", sans-serif;
    font-size: 29px;
  }

  .contact {
    left: 81px;
    top: 717px;
    font-size: 30px;
    line-height: 45.5px;
  }
  .contact p { margin: 0; }
  .label {
    font-family: "Roboto Condensed", "Arial Narrow", sans-serif;
    font-weight: 700;
    color: var(--accent-yellow);
  }
  .note {
    font-size: 24px;
    color: var(--accent-yellow);
  }

  .address {
    left: 81px;
    top: 1034px;
    font-size: 30px;
    line-height: 41px;
  }
  .address p { margin: 0; }

  .language-note {
    left: 625px;
    top: 1007px;
    font-size: 26px;
    transform: translate(-50%, -50%) rotate(-90deg);
  }
</style>
</head>
<body>
  <main class="card">
    <h1 class="doctor-name">
      <span>Dr. Eduardo</span>
      <span>Maximino</span>
      <span>Ortega</span>
      <span>Benavides</span>
    </h1>

    <p class="specialty">
      <span>Medicina general</span>
      <span>(Hospital Almendral)</span>
    </p>

    <p class="hours">Sábado y domingo 10:00 am a 10:00 pm</p>

    <div class="contact">
      <p><span class="label">Tel:</span> 471-5836</p>
      <p>555-917-4402 <span class="note">(Emergencias)</span></p>
      <p><span class="label">E-mail:</span> maximinoob@correoficticio.mx</p>
    </div>

    <div class="address">
      <p><span class="label">Address:</span> Calle Tomás Ocampo</p>
      <p>#247 Col. Almendral</p>
    </div>

    <p class="language-note">English Spoken</p>
  </main>
</body>
</html>
```